Labels for probiotic care products as Body Cream, Shower gel, Hand soap, ....

We are a starting a business in Flanders Belgium. We are looking for a label for care products, based on probiotics or good bacterie. We are looking for a fresh design that attracts people who wants a good product, based on naturally components. The products make that the microflora of the skin becomes and remains natural. The label must we be adaptive on bottles of 15 cm height to 8 cm height and a width of 4,5 cm. The brand name is KOVA REMU (beautiful skin in Hawaiian) or maybe just KOVA.

Industry/Entity Type

Business

Colors

Designer to choose colors to be used in the design.

Requirements
Must have
• somewhere the text "Probiotic Skin Care"
• I also have to tell that the bottles are white.
Nice to have
• I uploaded the 9 existing labels, but I want a totally new one, because the labels of our cleaning products are the same. I also uploaded a mood bord of labels I like.

```html
<!DOCTYPE html>
<html lang="en">
<head>
<meta charset="utf-8">
<title>KOVA Natural Skin Cream – Label</title>
<link href="https://fonts.googleapis.com/css2?family=Montserrat:wght@300;400;500;600&display=swap" rel="stylesheet">
<style>
  :root {
    --backdrop: #f1f1f1;
    --label-white: #ffffff;
    --brand-orange: #e8532a;
    --leaf-green: #2f7d3c;
    --text-dark-orange: #c9421f;
  }
  * { margin: 0; padding: 0; box-sizing: border-box; }
  html, body {
    width: 1200px;
    height: 900px;
    overflow: hidden;
    background: var(--backdrop);
    font-family: "Montserrat", sans-serif;
  }
  .canvas {
    position: relative;
    width: 1200px;
    height: 900px;
    display: flex;
    align-items: center;
    justify-content: center;
  }
  .label {
    position: relative;
    width: 320px;
    height: 840px;
    background: var(--label-white);
    border-radius: 6px;
  }
  .brand-mark {
    position: absolute;
    top: 110px;
    left: 0;
    right: 0;
    display: flex;
    flex-direction: column;
    align-items: center;
    gap: 12px;
  }
  .brand-mark__dot {
    width: 96px;
    height: 96px;
    border-radius: 50%;
    background: var(--brand-orange);
  }
  .brand-mark__name {
    font-weight: 500;
    font-size: 24px;
    letter-spacing: 3px;
    color: var(--brand-orange);
  }
  .wordmark {
    position: absolute;
    top: 345px;
    left: 0;
    right: 0;
    text-align: center;
  }
  .wordmark__name {
    font-weight: 300;
    font-size: 76px;
    line-height: 1;
    letter-spacing: 2px;
    color: var(--brand-orange);
  }
  .wordmark__product {
    margin-top: 8px;
    font-weight: 600;
    font-size: 18px;
    letter-spacing: 0.3px;
    color: var(--leaf-green);
  }
  .tagline {
    position: absolute;
    left: 22px;
    top: 768px;
    transform: rotate(-90deg);
    transform-origin: left top;
    font-weight: 400;
    font-size: 22px;
    letter-spacing: 0.5px;
    color: var(--brand-orange);
    white-space: nowrap;
  }
  .natural-badge {
    position: absolute;
    top: 640px;
    left: 50%;
    transform: translateX(-50%);
    width: 66px;
    height: 66px;
  }
  .net-volume {
    position: absolute;
    top: 748px;
    left: 0;
    right: 0;
    text-align: center;
    font-weight: 500;
    font-size: 18px;
    color: var(--text-dark-orange);
  }
</style>
</head>
<body>
  <main class="canvas">
    <section class="label">
      <div class="brand-mark">
        <span class="brand-mark__dot"></span>
        <span class="brand-mark__name">KOVA</span>
      </div>

      <div class="wordmark">
        <h1 class="wordmark__name">KOVA</h1>
        <p class="wordmark__product">NATURAL SKIN CREAM</p>
      </div>

      <p class="tagline">Probiotic Skin Care</p>

      <svg class="natural-badge" viewBox="0 0 66 66" aria-hidden="true">
        <circle cx="33" cy="33" r="31" fill="var(--leaf-green)"/>
        <circle cx="33" cy="33" r="25" fill="none" stroke="#ffffff" stroke-width="2"/>
      </svg>

      <p class="net-volume">Net Volume .50ml ℮</p>
    </section>
  </main>
</body>
</html>
```